Design a fresh new presentation folder for us!

We are looking for a fresh design of our new presentation folder.<br/><br/>We would like our current logo and colours being used in the design as well as images associated with our industry being international logistics.<br/><br/>Our services include, international freight - sea and air, domestic road transport, 3pl and warehousing.<br/><br/>We will attach our logo and other images we have used in the past to give you an idea of what we are after. Also attached our old folder.<br/><br/>We want a brand new fresh approach that is a really modern design. It needs to be visually striking.

Industry/Entity Type

Logistic

Colors
9ccb3b
acd037
cadf82
eef4d8

Requirements
Must have
• Fresh. Modern. Visually striking. Industry related.
• Slogan - Local Knowledge, Global Strength or Complete Logistics Solutions

```html
<!DOCTYPE html>
<html lang="en">
<head>
<meta charset="utf-8">
<title>Presentation Folder – Complete Logistics Solutions</title>
<link href="https://fonts.googleapis.com/css2?family=Titillium+Web:ital,wght@1,600;1,700&family=Lato:wght@400;700&display=swap" rel="stylesheet">
<style>
:root{
  --green:#8cc63f;
  --green-deep:#6db33f;
  --green-light:#cadf82;
  --green-pale:#eef4d8;
  --lime:#acd037;
  --cell-grey:#efefef;
  --table-line:#7a7a7a;
  --dieline:#2b3d7a;
  --ink:#333;
  --white:#fff;
}
*{margin:0;padding:0;box-sizing:border-box}
html,body{width:1200px;height:914px;overflow:hidden;background:#fff}
.canvas{position:relative;width:1200px;height:914px;font-family:'Lato',sans-serif}

/* front panel */
.panel{position:absolute;left:22px;top:22px;width:992px;height:674px;overflow:hidden;background:#fff}
.panel-green{position:absolute;left:0;top:0;width:620px;height:674px;
  background:linear-gradient(90deg,#7fbf3a 0%,#9ccb3b 40%,#cadf82 75%,rgba(238,244,216,0) 100%)}
.road{position:absolute;left:0;bottom:0;width:992px;height:150px;
  background:linear-gradient(180deg,rgba(255,255,255,0) 0%,rgba(156,203,59,.25) 40%,rgba(140,120,205,.55) 80%,rgba(120,100,195,.7) 100%)}
.road-streak{position:absolute;left:0;bottom:60px;width:992px;height:6px;
  background:linear-gradient(90deg,rgba(109,179,63,.9),rgba(109,179,63,.3) 60%,rgba(255,255,255,0))}
.fold-lines{position:absolute;left:490px;top:0;width:12px;height:674px;
  border-left:1px solid var(--dieline);border-right:1px solid var(--dieline)}
.fold-lines::after{content:"";position:absolute;left:4px;top:0;height:100%;border-left:1px solid var(--dieline)}

.slogan{position:absolute;left:26px;top:36px;width:436px;height:36px;background:var(--green-deep);
  box-shadow:3px 3px 0 rgba(0,0,0,.18);color:#fff;font-family:'Titillium Web',sans-serif;font-style:italic;
  font-weight:700;font-size:26px;line-height:36px;text-align:center;letter-spacing:-.3px}

.service{position:absolute;width:136px}
.service .photo{width:136px;height:136px;border:2px solid #fff;box-shadow:3px 3px 5px rgba(0,0,0,.3)}
.service .label{margin-top:14px;height:21px;background:var(--green-deep);color:#fff;
  font-family:'Titillium Web',sans-serif;font-style:italic;font-weight:600;font-size:11.5px;line-height:21px;
  text-align:center;box-shadow:3px 3px 0 rgba(0,0,0,.15);white-space:nowrap}

/* conversion tables */
.conv{position:absolute;border-collapse:collapse;font-size:9.6px;color:var(--ink)}
.conv th,.conv td{border:1px solid var(--table-line);height:13px;padding:0 4px;line-height:11px}
.conv th{background:var(--lime);font-weight:700;color:#222}
.conv th:first-child,.conv td:first-child{text-align:right}
.conv th:last-child,.conv td:last-child{text-align:left}
.conv tr:nth-child(odd) td{background:var(--green-light)}
.conv tr:nth-child(even) td{background:var(--cell-grey)}

/* hero truck area */
.truck{position:absolute;left:530px;top:262px;width:460px;height:378px;border-radius:18px 40px 10px 10px;
  background:linear-gradient(180deg,#f7f9f8 0%,#e9eeeb 55%,#cfdcd3 85%,#b7c9bc 100%);
  -webkit-mask-image:linear-gradient(90deg,#000 0%,#000 70%,rgba(0,0,0,0) 100%);
  mask-image:linear-gradient(90deg,#000 0%,#000 70%,rgba(0,0,0,0) 100%)}

.dieline{position:absolute;left:0;top:0}
</style>
</head>
<body>
<div class="canvas">
  <div class="panel">
    <div class="panel-green"></div>
    <div class="road"></div>
    <div class="road-streak"></div>
    <div class="truck" role="img" aria-label="White semi-trailer truck driving at speed on a highway"></div>
    <div class="fold-lines"></div>

    <div class="slogan">COMPLETE LOGISTICS SOLUTIONS</div>

    <div class="service" style="left:26px;top:86px">
      <div class="photo" role="img" aria-label="Passenger jet flying above clouds" style="background:linear-gradient(180deg,#4f7fbf,#a9c6e6 60%,#e6eef7)"></div>
      <div class="label">AIR FREIGHT</div></div>
    <div class="service" style="left:176px;top:86px">
      <div class="photo" role="img" aria-label="Container ship loaded with colourful containers at sea" style="background:linear-gradient(180deg,#4b8fc0 0%,#3b7fb0 30%,#c24c3c 55%,#d89a3a 75%,#3e6f9e)"></div>
      <div class="label">SEA FREIGHT</div></div>
    <div class="service" style="left:326px;top:86px">
      <div class="photo" role="img" aria-label="Truck on an open road at sunset" style="background:linear-gradient(180deg,#3b5a8c 0%,#c98a5a 50%,#6a6a72 75%,#3c3c44)"></div>
      <div class="label">DOMESTIC FREIGHT</div></div>

    <div class="service" style="left:26px;top:268px">
      <div class="photo" role="img" aria-label="Warehouse with tall stocked racking" style="background:linear-gradient(90deg,#b4562e,#d8a360 40%,#e3e6ea 60%,#b66532)"></div>
      <div class="label">3PL &amp; WAREHOUSING</div></div>
    <div class="service" style="left:176px;top:268px">
      <div class="photo" role="img" aria-label="Officers inspecting a shipping container door" style="background:linear-gradient(90deg,#2f5f95,#3e74ad 60%,#6d8a55)"></div>
      <div class="label">CUSTOMS &amp; QUARANTINE</div></div>
    <div class="service" style="left:326px;top:268px">
      <div class="photo" role="img" aria-label="Tanker truck under a blue sky" style="background:linear-gradient(180deg,#2f5ea8,#8fb3df 45%,#c6ccd3 65%,#5f6368)"></div>
      <div class="label">SPECIALISED CARGO</div></div>

    <div class="service" style="left:26px;top:451px">
      <div class="photo" role="img" aria-label="Rows of laboratory vials" style="background:linear-gradient(180deg,#1f3fbf,#5d86e0 50%,#e4ecfb)"></div>
      <div class="label">PHARMACEUTICAL FREIGHT</div></div>
    <div class="service" style="left:176px;top:451px">
      <div class="photo" role="img" aria-label="Pile of fresh strawberries" style="background:radial-gradient(circle at 50% 50%,#e3342c,#b51a1e 70%,#7a1014)"></div>
      <div class="label">PERISHABLE FREIGHT</div></div>
    <div class="service" style="left:326px;top:451px">
      <div class="photo" role="img" aria-label="Business person reviewing charts on a tablet" style="background:linear-gradient(135deg,#e8eef4,#9fb4c8 55%,#2f4a6a)"></div>
      <div class="label">CONSULTANCY</div></div>

    <table class="conv" style="left:518px;top:36px;width:198px">
      <tr><th>Lenght</th><th style="width:64px">Multiply By</th></tr>
      <tr><td>Inches to Centimetres</td><td>2.54</td></tr>
      <tr><td>Centimetres to Inches</td><td>0.39</td></tr>
      <tr><td>Inches to Millimetres</td><td>25.40</td></tr>
      <tr><td>Milimetres to Inches</td><td>0.04</td></tr>
      <tr><td>Feet to Metres</td><td>0.31</td></tr>
      <tr><td>Metres to Feet</td><td>3.28</td></tr>
    </table>
    <table class="conv" style="left:729px;top:36px;width:239px">
      <tr><th>Area</th><th style="width:64px">Multiply By</th></tr>
      <tr><td>Square Inches to Square Centimetres</td><td>6.451</td></tr>
      <tr><td>Square Centimetres to Square Inches</td><td>0.15</td></tr>
      <tr><td>Square Feet to Square Metres</td><td>0.09</td></tr>
      <tr><td>Square Metres to Square Feet</td><td>10.76</td></tr>
      <tr><td>Square Yards to Square Metres</td><td>0.84</td></tr>
      <tr><td>&nbsp;</td><td></td></tr>
    </table>
    <table class="conv" style="left:518px;top:140px;width:198px">
      <tr><th>Weight</th><th style="width:64px">Multiply By</th></tr>
      <tr><td>Pounds to Kilograms</td><td>0.45</td></tr>
      <tr><td>Kilograms to Pounds</td><td>2.21</td></tr>
      <tr><td>Ounces to Grams</td><td>28.35</td></tr>
      <tr><td>Grams to Ounces</td><td>0.04</td></tr>
      <tr><td>Long Tons to Tonnes</td><td>1.02</td></tr>
      <tr><td>Tonnes to Long Tons</td><td>0.98</td></tr>
      <tr><td>Short Tons to Tonnes</td><td>0.91</td></tr>
      <tr><td>Tonnes to Short Tons</td><td>1.10</td></tr>
    </table>
    <table class="conv" style="left:729px;top:140px;width:239px">
      <tr><th>Volume</th><th style="width:64px">Multiply By</th></tr>
      <tr><td>Cubic Inches to Cubic Centimetres</td><td>16.39</td></tr>
      <tr><td>Cubic Centimetres to Cubic Inches</td><td>0.06</td></tr>
      <tr><td>Cubic Feet to Cubic Metres</td><td>0.03</td></tr>
      <tr><td>Cubic Metres to Cubic Feet</td><td>35.32</td></tr>
      <tr><td>Cubic Yards to Cubic Metres</td><td>0.76</td></tr>
      <tr><td>Cubic Metres to Cubic Yards</td><td>1.31</td></tr>
      <tr><td>Cubic Inches to Litres</td><td>0.02</td></tr>
      <tr><td>Litres to Cubic Inches</td><td>61.03</td></tr>
    </table>
  </div>

  <svg class="dieline" width="1200" height="914" viewBox="0 0 1200 914" fill="none" stroke="#2b3d7a" stroke-width="1">
    <rect x="22" y="22" width="992" height="674"/>
    <path d="M1014 196 H1024 C1060 196 1080 230 1090 290 L1178 638 L1014 694"/>
    <line x1="1022" y1="196" x2="1022" y2="694"/>
    <line x1="1060" y1="640" x2="1098" y2="552"/>
    <path d="M535 696 V792 C640 840 760 880 884 890 L938 858 C960 840 995 835 992 800 C990 770 970 770 970 760 L1011 706"/>
    <line x1="535" y1="704" x2="1011" y2="704"/>
    <line x1="662" y1="748" x2="697" y2="714"/>
    <line x1="834" y1="714" x2="868" y2="748"/>
    <line x1="662" y1="810" x2="697" y2="844"/>
    <line x1="834" y1="844" x2="868" y2="810"/>
  </svg>
</div>
</body>
</html>
```